Business card design needed

OH&S consultancy and training

Industry/Entity Type

Training

Contact Information for Business Card

Coastal Hazard & Skills Collective
Dorian Whitfield
Director

0427 391 608
dorian.whitfield@hzcollect.com.au
hzcollect.com.au

Ph: 03 9172 4309
Fx: 03 9172 4311

```html
<!DOCTYPE html>
<html lang="en">
<head>
<meta charset="utf-8">
<title>HZ Collect – Business Card</title>
<link href="https://fonts.googleapis.com/css2?family=Montserrat:wght@500;700&display=swap" rel="stylesheet">
<style>
  :root {
    --card-orange: #fbb012;
    --band-orange: #eaa20c;
    --ink: #2b2d3a;
  }
  * { box-sizing: border-box; margin: 0; padding: 0; }
  html, body {
    width: 1200px; height: 741px; overflow: hidden;
    background: #ffffff;
  }
  .card {
    position: relative;
    width: 1200px; height: 741px;
    background: var(--card-orange);
    font-family: "Montserrat", sans-serif;
    color: var(--ink);
  }
  .identity {
    position: absolute;
    left: 40px; top: 316px;
    width: 560px;
    text-align: center;
    font-weight: 700;
    text-transform: uppercase;
    letter-spacing: 4px;
    font-size: 37px;
    line-height: 54px;
  }
  .identity h1 { font-size: inherit; font-weight: inherit; }
  .contact {
    position: absolute;
    left: 38px; top: 652px;
    width: 890px;
    font-weight: 500;
    font-size: 17px;
    line-height: 28px;
    text-transform: uppercase;
    white-space: nowrap;
  }
  .contact .details { letter-spacing: 1.2px; }
  .contact .company { letter-spacing: 12.6px; }
  .contact .lines { letter-spacing: 3px; }
  .brand-band {
    position: absolute;
    left: 947px; top: 0;
    width: 218px; height: 741px;
    background: var(--band-orange);
    display: flex;
    align-items: flex-end;
    justify-content: center;
    padding-bottom: 52px;
  }
  .brand {
    display: flex;
    align-items: center;
    gap: 12px;
    font-weight: 700;
    font-size: 22px;
    letter-spacing: 2px;
    color: var(--ink);
    white-space: nowrap;
  }
  .brand-square {
    width: 18px; height: 18px;
    background: var(--ink);
  }
</style>
</head>
<body>
  <main class="card">
    <section class="identity">
      <h1 class="person-name">Dorian Whitfield</h1>
      <p class="person-title">Director</p>
    </section>

    <section class="contact">
      <p class="details">Contact details: 0427 391 608 dorian.whitfield@hzcollect.com.au</p>
      <p class="company">Coastal Hazard &amp; Skills Collective</p>
      <p class="lines">Web: hzcollect.com.au Ph: 03 9172 4309 Fx: 03 9172 4311</p>
    </section>

    <aside class="brand-band">
      <div class="brand">
        <span class="brand-square"></span>
        <span class="brand-name">HZ COLLECT</span>
      </div>
    </aside>
  </main>
</body>
</html>
```